Conference Header for use in marketing and on website

I need a header designed that promotes an event we will be holding to be used on marketing and website. I have attached a brief with the information that needs to be on it including the colours required. It will need to include an image of Melbourne at least and our logo. If you find a better Melbourne image you wish to use, I can purchase it off Quillmark Images.

I want it to be eyecatching and exciting and vibrant while still providing the details clearly. I also want source files included.

```html
<!DOCTYPE html>
<html lang="en">
<head>
<meta charset="utf-8">
<title>Spinform 2022 Conference Header</title>
<link href="https://fonts.googleapis.com/css2?family=Poppins:wght@400;500;600;700&display=swap" rel="stylesheet">
<style>
  :root {
    --page-bg: #f4f4f6;
    --purple-deep: #3a1968;
    --purple-mid: #5a1f82;
    --purple-bright: #6c2590;
    --cyan: #2fbdf0;
    --white: #ffffff;
    --dot-blue: #5b7fd6;
    --ring: #eeeef2;
  }
  * { margin: 0; padding: 0; box-sizing: border-box; }
  html, body {
    width: 1200px; height: 609px; overflow: hidden;
    background: var(--page-bg);
    font-family: "Poppins", sans-serif;
  }
  .stage {
    width: 1200px; height: 609px;
    display: flex; align-items: center; justify-content: center;
  }
  .header-banner {
    position: relative; width: 1200px; height: 452px; overflow: hidden;
    background: linear-gradient(100deg, var(--purple-deep) 0%, var(--purple-mid) 55%, var(--purple-bright) 100%);
    color: var(--white);
  }
  .city-haze {
    position: absolute; left: 0; top: 190px; width: 1200px; height: 262px;
    background:
      linear-gradient(90deg, rgba(58,25,104,0) 55%, var(--purple-bright) 85%),
      linear-gradient(180deg, rgba(255,255,255,0) 0%, rgba(120,80,150,0.16) 45%, rgba(40,15,70,0.22) 100%);
  }
  .event-title {
    position: absolute; left: 52px; top: 38px;
    font-size: 84px; font-weight: 600; line-height: 1; letter-spacing: -1px;
  }
  .event-subtitle {
    position: absolute; left: 53px; top: 130px;
    font-size: 37px; font-weight: 400; color: var(--cyan); line-height: 1;
  }
  .event-dates {
    position: absolute; left: 53px; top: 176px;
    font-size: 37px; font-weight: 500; line-height: 1;
  }
  .event-location {
    position: absolute; left: 53px; top: 250px;
    font-size: 41px; font-weight: 600; line-height: 1;
  }
  .year-tab {
    position: absolute; left: 517px; top: 0; width: 54px; height: 160px;
    background: var(--cyan);
    display: flex; align-items: center; justify-content: center;
  }
  .year-tab span {
    transform: rotate(-90deg);
    font-size: 50px; font-weight: 700; color: var(--purple-mid); line-height: 1;
  }
  .organiser {
    position: absolute; left: 54px; top: 370px;
    display: flex; align-items: center; gap: 10px;
  }
  .organiser-mark {
    width: 48px; height: 48px; border-radius: 50%; background: var(--white);
  }
  .organiser-text { display: flex; flex-direction: column; line-height: 1; }
  .organiser-name { font-size: 38px; font-weight: 500; letter-spacing: 1px; }
  .organiser-tag { font-size: 6px; font-weight: 500; margin-top: 3px; }
  .photo-cluster { position: absolute; left: 0; top: 0; }
</style>
</head>
<body>
<div class="stage">
  <section class="header-banner">
    <div class="city-haze" role="img" aria-label="Faint Melbourne skyline behind the text"></div>

    <h1 class="event-title">Spinform</h1>
    <p class="event-subtitle">Conference &amp; Exhibition</p>
    <p class="event-dates">18 – 20 September</p>
    <p class="event-location">Melbourne, Australia</p>

    <div class="year-tab"><span>2022</span></div>

    <div class="organiser">
      <div class="organiser-mark"></div>
      <div class="organiser-text">
        <span class="organiser-name">CASTWELL</span>
        <span class="organiser-tag">Rotary Casting Guild</span>
      </div>
    </div>

    <svg class="photo-cluster" width="1200" height="452" viewBox="0 0 1200 452">
      <defs>
        <linearGradient id="cityGrad" x1="0" y1="0" x2="0" y2="1">
          <stop offset="0" stop-color="#4f8fd8"/>
          <stop offset="0.45" stop-color="#b9cbe0"/>
          <stop offset="0.7" stop-color="#c99a55"/>
          <stop offset="1" stop-color="#c8c8c6"/>
        </linearGradient>
        <linearGradient id="roomGradA" x1="0" y1="0" x2="1" y2="1">
          <stop offset="0" stop-color="#7d7f88"/>
          <stop offset="1" stop-color="#2e3142"/>
        </linearGradient>
        <linearGradient id="roomGradB" x1="0" y1="0" x2="0" y2="1">
          <stop offset="0" stop-color="#c9cdd6"/>
          <stop offset="1" stop-color="#3f5a6e"/>
        </linearGradient>
      </defs>
      <circle cx="986" cy="79" r="268" fill="var(--ring)"/>
      <circle cx="986" cy="79" r="262" fill="url(#cityGrad)" role="img" aria-label="Photo of a domed Melbourne railway station under a blue sky"/>

      <circle cx="694" cy="283" r="19" fill="var(--dot-blue)"/>

      <circle cx="730" cy="173" r="68" fill="var(--ring)"/>
      <circle cx="730" cy="173" r="63" fill="url(#roomGradA)" role="img" aria-label="Photo of delegates talking at a conference table"/>

      <circle cx="830" cy="307" r="84" fill="var(--ring)"/>
      <circle cx="830" cy="307" r="78" fill="url(#roomGradB)" role="img" aria-label="Photo of a full conference dining hall"/>
    </svg>
  </section>
</div>
</body>
</html>
```